Nightclub-type Event Poster Advertisement

Lumora Events is based in Christchurch, New Zealand and we have our next party coming up. We like a different flair for each of our events so are looking for some help from you guys. We are very flexible with everything - colours, layout, backgrounds, fonts, etc so it's ALL up to you. Attached is our company logo and the flyer (and poster) we used for our last party. Our website is lumoranz.example where you can find and use our photos and find more info about us if you desire.
Designs we are wanting: An A3 poster,an A6 flyer (smaller version of the poster is probably fine), tickets (140x68 mm). It would be great if a 5 mm bleed was included so we could get them printed directly.
Details for the event to be advertised are as followed:
Party Name: (TBD... will update ASAP)
05/07/2014
10pm-close
Lineup: 'Bazzo (Akl)', 'DJ Glimtrax', 'DJ's Morquent & Pelnavo', 'Quiet Harbour Pulse'.
Dorrin Hattles Central, Corner Fenwick & Oberly Streets
$10 Tickets
R18
Tickets & Enquiries: Marta on 0219047362
Presented by Lumora Entertainment
Thanks to everyone who reads this and please give it a go! Any questions don't hesitate to ask.
Target Market(s)
New Zealand Europeans in Christchurch, New Zealand between 18 and 25 years old.
Industry/Entity Type
Events
Look and feel

```html
<!DOCTYPE html>
<html lang="en">
<head>
<meta charset="utf-8">
<title>Lumora Events – 05/07/2014</title>
<link href="https://fonts.googleapis.com/css2?family=Audiowide&family=Russo+One&display=swap" rel="stylesheet">
<style>
  :root {
    --space-deep: #0b1030;
    --space-blue: #1d3a8a;
    --space-violet: #4a2f8f;
    --space-magenta: #8a4fa8;
    --space-glow: #e8a58c;
    --ink: #000000;
    --white: #ffffff;
    --cream: #f6e6a6;
    --muted: #6d6f86;
    --title-a: #3c77c4;
    --title-b: #f3e4b6;
    --title-c: #5a8fd6;
  }
  html, body {
    margin: 0;
    padding: 0;
    width: 849px;
    height: 1200px;
    overflow: hidden;
    background: var(--space-deep);
  }
  .poster {
    position: relative;
    width: 849px;
    height: 1200px;
    overflow: hidden;
    font-family: "Audiowide", sans-serif;
    color: var(--white);
  }
  .backdrop {
    position: absolute;
    inset: 0;
    background:
      radial-gradient(ellipse 45% 30% at 80% 72%, rgba(232,165,140,0.55), transparent 70%),
      radial-gradient(ellipse 60% 40% at 70% 55%, rgba(138,79,168,0.7), transparent 75%),
      radial-gradient(ellipse 60% 35% at 25% 20%, rgba(60,110,190,0.6), transparent 75%),
      linear-gradient(170deg, var(--space-blue) 0%, var(--space-deep) 35%, var(--space-violet) 70%, var(--space-deep) 100%);
  }
  .event-date {
    position: absolute;
    top: 52px;
    left: 0;
    width: 100%;
    text-align: center;
    font-size: 44px;
    letter-spacing: 3px;
    margin: 0;
  }
  .lineup-disc {
    position: absolute;
    left: 0;
    top: 0;
  }
  .brand-mark {
    position: absolute;
    top: 318px;
    left: 0;
    width: 100%;
    text-align: center;
    font-size: 18px;
    letter-spacing: 3px;
    color: var(--white);
  }
  .party-title {
    position: absolute;
    top: 398px;
    left: 0;
    width: 100%;
    margin: 0;
    text-align: center;
    font-family: "Russo One", sans-serif;
    font-size: 92px;
    letter-spacing: 3px;
    background: linear-gradient(90deg, var(--title-a) 0%, var(--title-c) 30%, var(--title-b) 60%, var(--title-a) 100%);
    -webkit-background-clip: text;
    background-clip: text;
    color: transparent;
  }
  .headliner {
    position: absolute;
    top: 522px;
    left: 0;
    width: 100%;
    margin: 0;
    text-align: center;
    font-family: "Russo One", sans-serif;
    font-size: 52px;
    letter-spacing: 2px;
  }
  .support-acts {
    position: absolute;
    top: 612px;
    left: 0;
    width: 100%;
    margin: 0;
    padding: 0;
    list-style: none;
    text-align: center;
    font-family: "Russo One", sans-serif;
    font-size: 31px;
    line-height: 40px;
    letter-spacing: 1px;
  }
  .bolt {
    position: absolute;
    left: 340px;
    top: 775px;
  }
  .entry-info {
    position: absolute;
    left: 70px;
    top: 858px;
    margin: 0;
    font-size: 38px;
    line-height: 56px;
  }
  .entry-info .value { color: var(--cream); }
  .entry-info .label {
    color: var(--muted);
    -webkit-text-stroke: 1px #b9bbd0;
  }
  .venue {
    position: absolute;
    left: 505px;
    width: 270px;
    top: 852px;
    margin: 0;
    text-align: center;
    font-size: 26px;
    line-height: 33px;
    font-style: normal;
  }
  .presenter-name {
    position: absolute;
    right: 62px;
    top: 1000px;
    text-align: right;
    font-size: 26px;
    line-height: 34px;
    color: var(--white);
  }
  .credits {
    position: absolute;
    left: 70px;
    top: 1090px;
    margin: 0;
    font-size: 22px;
    line-height: 54px;
  }
  .credits .contact-name { color: var(--cream); }
</style>
</head>
<body>
<main class="poster">
  <div class="backdrop" role="img" aria-label="Starry deep-space galaxy background in blue, violet and warm pink tones"></div>

  <p class="event-date">05/07/2014</p>

  <svg class="lineup-disc" width="849" height="1200" viewBox="0 0 849 1200" aria-hidden="true">
    <circle cx="425" cy="470" r="322" fill="none" stroke="var(--ink)" stroke-width="5"/>
    <circle cx="425" cy="470" r="308" fill="var(--ink)"/>
  </svg>

  <div class="brand-mark">LUMORA EVENTS</div>

  <h1 class="party-title">TITLE HERE</h1>
  <h2 class="headliner">BAZZO (AKL)</h2>
  <ul class="support-acts">
    <li>DJ GLIMTRAX</li>
    <li>DJ'S MORQUENT &amp; PELNAVO</li>
    <li>QUIET HARBOUR PULSE</li>
  </ul>

  <svg class="bolt" width="110" height="215" viewBox="0 0 110 215" aria-hidden="true">
    <polygon points="98,0 22,92 62,102 4,215 92,112 50,100 110,8" fill="var(--ink)"/>
  </svg>

  <p class="entry-info">
    <span class="value">R18</span><br>
    <span class="value">$10</span> <span class="label">Tickets</span><br>
    <span class="value">10 pm</span> <span class="label">close</span>
  </p>

  <address class="venue">
    Dorrin Hattles Central<br>
    Corner Fenwick &amp;<br>
    Oberly Streets
  </address>

  <div class="presenter-name">Lumora<br>Events</div>

  <p class="credits">
    Presented by Lumora Entertainment<br>
    Tickets &amp; Enquiries: <span class="contact-name">Marta</span> on 0219047362
  </p>
</main>
</body>
</html>
```